Upmarket Bathroom and Kitchen ware supplier needs a classy business card design

We are a company based in Fiji, we sell plumbing ware (Kitchen and bathroom taps, Basins,showers, toilets etc) through up market show rooms to individuals and directly through Architects and designers of resorts and holiday houses for new builds and renovations. we are wanting to upgrade our over all look and brand. we are starting with a new logo but will be rebranding the whole business. This project is for a business card design for my management and tales team I would like it to be dark, classy and interesting

Target Market(s)

Resort directors and Management, High end holiday home owners

Contact Information for Business Card

Neil Dawson
Director
+64219473815

Colors

Designer to choose colors to be used in the design.

Requirements
Must have
• Must have an upmarket appearance I like darker charcoal shades but will be guided by the designers
• Please any catch phrases like "Crafting remarkable living rooms" this belongs tpo one of our suppliers so can not be used.
Nice to have
• Double sided, so front dedicated to logo provided and back info about the business and the person.

```html
<!DOCTYPE html>
<html lang="en">
<head>
<meta charset="utf-8">
<title>Corvale Interiors – Business Card</title>
<link rel="stylesheet" href="https://fonts.googleapis.com/css2?family=Lato:wght@300;400;700&display=swap">
<style>
  :root {
    --backdrop: #9b9b9b;
    --paper: #ffffff;
    --charcoal: #2b2b2b;
    --ink: #1e1e1e;
    --ink-soft: #3a3a3a;
    --rule: #6a6a6a;
    --light-text: #f2f2f2;
    --light-rule: #8a8a8a;
  }
  * { margin: 0; padding: 0; box-sizing: border-box; }
  html, body {
    width: 1200px;
    height: 1200px;
    overflow: hidden;
    background: var(--backdrop);
    font-family: "Lato", Arial, sans-serif;
  }
  .canvas { position: relative; width: 1200px; height: 1200px; }

  .card {
    position: absolute;
    left: 199px;
    width: 803px;
    height: 459px;
  }
  .card--front { top: 85px; background: var(--paper); color: var(--ink); }
  .card--back { top: 655px; background: var(--charcoal); color: var(--light-text); }

  /* Brand lockup */
  .brand {
    position: absolute;
    display: flex;
    align-items: center;
    gap: 22px;
  }
  .brand__dot {
    width: 14px;
    height: 14px;
    border-radius: 50%;
    background: currentColor;
    flex: none;
  }
  .brand__name {
    font-weight: 300;
    letter-spacing: 0.32em;
    text-transform: uppercase;
    line-height: 1.35;
    white-space: nowrap;
  }
  .card--front .brand { right: 54px; top: 80px; }
  .card--front .brand__name { font-size: 22px; }
  .card--back .brand { left: 50%; top: 50%; transform: translate(-50%, -50%); }
  .card--back .brand__name { font-size: 30px; }

  /* Contact block */
  .person {
    position: absolute;
    left: 54px;
    top: 326px;
    display: flex;
    align-items: baseline;
    gap: 16px;
  }
  .person__name {
    font-weight: 700;
    font-size: 21px;
    letter-spacing: 0.06em;
    text-transform: uppercase;
  }
  .person__role {
    font-size: 18px;
    color: var(--ink-soft);
  }
  .person__role::before {
    content: "|";
    font-weight: 700;
    margin-right: 10px;
    color: var(--ink);
  }
  .divider {
    position: absolute;
    left: 54px;
    top: 366px;
    width: 580px;
    height: 1px;
    background: var(--rule);
  }
  .contact {
    position: absolute;
    left: 54px;
    top: 382px;
    font-size: 18px;
    color: var(--ink-soft);
    list-style: none;
    display: flex;
    gap: 10px;
    white-space: nowrap;
  }
  .contact__label { font-weight: 700; color: var(--ink); }
  .contact__sep { color: var(--ink-soft); }
</style>
</head>
<body>
<main class="canvas">
  <section class="card card--front" aria-label="Business card front">
    <div class="brand">
      <span class="brand__dot"></span>
      <span class="brand__name">Corvale Interiors</span>
    </div>
    <div class="person">
      <span class="person__name">Adam Fletcher</span>
      <span class="person__role">President</span>
    </div>
    <div class="divider"></div>
    <ul class="contact">
      <li><span class="contact__label">P.</span> +3120 5518 204</li>
      <li class="contact__sep">/</li>
      <li><span class="contact__label">E.</span> info@corvale.com</li>
      <li class="contact__sep">/</li>
      <li><span class="contact__label">W.</span> www.corvale.com</li>
    </ul>
  </section>

  <section class="card card--back" aria-label="Business card back">
    <div class="brand">
      <span class="brand__dot"></span>
      <span class="brand__name">Corvale Interiors</span>
    </div>
  </section>
</main>
</body>
</html>
```